Pacific Screen Trade Alliance is preparing a regular newsletter and needs a design

Our association is made up of media companies, TV stations and video on demand companies. As an association our role is to bring industry together to engage in government dialogues, fight video piracy and hold conferences and events. We are starting a regular newsletter to let our members know what activities we have been undertaking on their behalf and what upcoming activities there are. It will be a combination of text and pictures/ graphics. We have made a lot of changes to the association so we need a design which is professional looking, but also creative and future looking. It should also have a sense of entertainment given it is the video entertainment industry we represent. Attached is an example of a recent newsletter but would like to see something a little more dynamic and professional.

Target Market(s)

Executives in media companies

Font styles to use
Serif

Colors

Designer to choose colors to be used in the design.

Requirements
Must have
• A combination of text, photos and graphics in a modern, personable yet professional layout and design

```html
<!DOCTYPE html>
<html lang="en">
<head>
<meta charset="utf-8">
<title>Policy &amp; Piracy Newsletter – Pacific Screen Trade Alliance</title>
<link rel="stylesheet" href="https://fonts.googleapis.com/css2?family=Oswald:wght@400;500;600&family=Josefin+Sans:wght@400;600&display=swap">
<style>
:root{
  --red:#d0202e;
  --red-deep:#b3151f;
  --red-dark:#8e0f18;
  --pink:#f6dcdf;
  --pink-soft:#fbeef0;
  --white:#ffffff;
  --ink:#333333;
  --bar-grey:#cfd6e6;
  --bg:#ffffff;
}
*{margin:0;padding:0;box-sizing:border-box}
html,body{width:1200px;height:1000px;overflow:hidden;background:var(--bg)}
body{position:relative;font-family:"Josefin Sans",Arial,sans-serif;color:var(--ink)}
.spread,.page,.photo,.abs{position:absolute}
.spread{overflow:hidden}
.page{top:0;height:100%;overflow:hidden}
.heading{font-family:"Oswald","Arial Narrow",sans-serif;font-weight:500;text-transform:uppercase;letter-spacing:.2px}
.body-copy{font-size:6px;line-height:7.6px;text-align:justify;overflow:hidden}
.body-copy p+p{margin-top:6px}
.on-red{color:var(--white)}
.page-no{position:absolute;bottom:10px;font-family:"Oswald",sans-serif;font-size:9px;color:var(--red);display:flex;align-items:center;gap:3px}
.page-no.light{color:var(--white)}
.page-no b{font-weight:500;writing-mode:vertical-rl;transform:rotate(180deg);font-size:5px}
.page-no i{display:block;width:1px;height:14px;background:currentColor}
.quote{font-family:"Oswald",sans-serif;font-weight:400;color:var(--white);text-transform:uppercase;font-size:15px;line-height:22px;letter-spacing:.6px}
.stripes{background:repeating-linear-gradient(115deg,rgba(255,255,255,0) 0 38px,rgba(255,255,255,.07) 38px 60px)}

/* cover */
.cover-back{left:0;width:290px;background:var(--red)}
.cover-back .intro{left:44px;top:66px;width:206px;text-align:center;font-size:6px;line-height:8.2px}
.more-info{left:0;width:290px;top:372px;text-align:center;font-size:7px;color:var(--white)}
.more-info .heading{font-size:7.5px;font-weight:600;margin-bottom:2px}
.cover-front{left:290px;width:290px;background:linear-gradient(160deg,#2a1b5e 0%,#3f2a9a 35%,#1b1440 70%,#0d0a22 100%)}
.masthead{left:18px;top:34px;border-left:2px solid var(--white);padding-left:6px;color:var(--white)}
.masthead .kicker{font-size:14px;line-height:15px;font-weight:400}
.masthead .title{font-size:27px;line-height:28px;font-weight:500}
.edition{left:18px;top:376px;font-size:6.8px;line-height:8px;color:var(--white)}
.brand{left:172px;top:350px;text-align:left}
.brand .name{font-family:"Oswald",sans-serif;font-weight:500;font-size:34px;line-height:34px;color:var(--red);letter-spacing:1px}
.brand .full{font-size:5px;color:var(--white);letter-spacing:.3px;margin-top:2px}

/* contents */
.contents-left{left:0;width:290px;background:var(--white)}
.contents-left .intro{left:22px;top:331px;width:254px;font-size:6.2px;line-height:8.2px;text-align:center}
.contents-right{left:290px;width:290px;background:var(--red)}
.toc-title{left:172px;top:160px;font-size:15px;color:var(--white)}
.toc-item{position:absolute;right:12px;display:flex;gap:6px;align-items:stretch;color:var(--white)}
.toc-item .txt{text-align:right;font-size:6.4px;line-height:8.4px}
.toc-item .txt strong{display:block;font-family:"Oswald",sans-serif;font-weight:500;font-size:8px;line-height:10px}
.toc-item .num{border-left:1px solid var(--white);padding-left:5px;font-family:"Oswald",sans-serif;font-size:10px;display:flex;flex-direction:column;justify-content:center;line-height:10px}
.toc-item .num small{font-size:5px}

/* feature spread */
.feature-left{left:0;width:290px;background:var(--red)}
.feature-left .title{left:29px;top:17px;font-size:13px;color:var(--white)}
.col-a{left:29px;top:44px;width:130px;height:136px}
.col-b{left:29px;top:186px;width:130px;height:31px}
.col-c{left:29px;top:222px;width:260px;height:31px}
.drone-photo{left:29px;top:258px;width:124px;height:132px;background:linear-gradient(180deg,#f2a23c 0%,#e8761f 55%,#6b2a0c 100%)}
.feature-left .quote{left:160px;top:262px;width:118px;text-align:right}
.feature-right{left:290px;width:290px;background:var(--white)}
.feature-right .title{left:24px;top:218px;font-size:13px;color:var(--red)}
.col-d{left:24px;top:244px;width:236px;height:96px;color:var(--ink)}
.callout{left:24px;top:348px;width:236px;height:40px;background:var(--red);color:var(--white);font-size:6px;line-height:8px;text-align:center;padding:6px 10px}

/* data spread */
.data-left{left:0;width:290px;background:linear-gradient(120deg,var(--pink-soft),var(--white) 40%,var(--pink) 100%)}
.data-left .title{left:28px;top:17px;font-size:13px;color:var(--red)}
.col-e{left:28px;top:44px;width:240px;height:69px;color:var(--ink)}
.col-f{left:28px;top:116px;width:240px;height:16px}
.lights-photo{left:46px;top:140px;width:212px;height:72px;background:linear-gradient(90deg,#f4f4f4,#e6e6e6 50%,#f4f4f4)}
.col-g{left:28px;top:226px;width:240px;height:24px}
.data-left .title2{left:28px;top:268px;font-size:13px;color:var(--red)}
.chart{left:28px;top:296px;width:126px}
.chart-row{display:flex;align-items:center;height:7.5px;gap:4px}
.chart-row span{font-size:5px;width:22px;color:#888}
.chart-row .track{flex:1;height:4px;background:var(--bar-grey);position:relative}
.chart-row .fill{position:absolute;left:0;top:0;height:100%}
.col-h{left:163px;top:296px;width:105px;height:86px}
.data-right{left:290px;width:290px;background:linear-gradient(160deg,#e55a8a 0%,#c8233a 30%,#b8152a 60%,#7a1320 100%)}
.data-right .quote{left:186px;top:245px;width:92px;text-align:right}
</style>
</head>
<body>

<section class="spread" style="left:8px;top:84px;width:580px;height:409px" aria-label="Cover spread">
  <div class="page cover-back stripes">
    <div class="abs intro on-red">
      <p>PACIFIC SCREEN TRADE ALLIANCE,<br>elit eget fringilla congue, erat neque interdum neque, at hendrerit erat tortor id erat. Nullam rhoncus dui et pretium scelerisque. Pellentesque facilisis pharetra quam a mollis. Vestibulum luctus massa sem. Vestibulum sapien nibh, scelerisque eu accumsan ut, porttitor eget nisi. Curabitur magna ex, aliquam non tincidunt ut, fringilla ac elit. Donec viverra malesuada lorem nec ultricies. Phasellus pellentesque nisi et enim scelerisque, a posuere neque lobortis. Morbi sed fermentum lectus. Integer malesuada tellus eget facilisis malesuada. Sed vitae viverra lorem. In ante lacus, vulputate aliquet urna vitae, ultrices fringilla urna. Donec cursus lorem eros. Nulla posuere scelerisque ex, eget scelerisque lectus facilisis nec. Fusce a lorem id justo ornare dictum at non orci.</p>
    </div>
    <div class="abs more-info">
      <div class="heading">For more information</div>
      <div>www.pacificscreen.org</div>
    </div>
  </div>
  <div class="page cover-front" role="img" aria-label="Photo of a professional video camera with flip-out screen under blue and red stage light">
    <svg class="abs" style="left:0;top:0" width="290" height="409" aria-hidden="true">
      <polygon points="120,0 175,0 70,409 20,409" fill="#d0202e" opacity=".55"/>
      <polygon points="175,0 200,0 95,409 70,409" fill="#7a3cc4" opacity=".35"/>
    </svg>
    <div class="abs masthead heading">
      <div class="kicker">Policy &amp; Piracy</div>
      <div class="title">Newsletter</div>
    </div>
    <div class="abs edition">SPRING 2019<br>SPECIAL EDITION</div>
    <div class="abs brand">
      <div class="name">PSTA</div>
      <div class="full">PACIFIC SCREEN TRADE ALLIANCE</div>
    </div>
  </div>
</section>

<section class="spread" style="left:612px;top:84px;width:580px;height:409px" aria-label="Contents spread">
  <div class="page contents-left">
    <div class="photo" style="left:0;top:0;width:290px;height:320px;background:linear-gradient(150deg,#6a6f78,#3b3f47 50%,#22252b);clip-path:polygon(0 0,100% 0,100% 62%,0 100%)" role="img" aria-label="Photo of hands using a laptop streaming a sports match"></div>
    <svg class="abs" style="left:0;top:200px" width="290" height="130" aria-hidden="true">
      <polygon points="290,0 290,30 0,130 0,120" fill="#f4c8cd" opacity=".8"/>
    </svg>
    <div class="abs intro">
      <p>The last few months have seen important anti-piracy initiatives by several Asian governments. They are a clear indication that goverments are seriously grappling with the ISD/app piracy ecosystems. We've seen stepped-up enforcement, policy announcements, and legislative movement.<br>(Now, if we could just get all of this in every country!)</p>
      <p style="margin-top:8px">For everyone's convenience, we've brought together some short descriptions in this Special Edition of our Policy and Piracy Newsletter.</p>
    </div>
  </div>
  <div class="page contents-right">
    <div class="photo" style="left:0;top:0;width:290px;height:409px;background:linear-gradient(170deg,#a8343c,#c9414a 40%,#d0202e);clip-path:polygon(0 0,100% 0,100% 36%,0 58%)" role="img" aria-label="Faded photo of a crowd holding flags at an event"></div>
    <div class="abs toc-title heading">In this issue</div>
    <div class="toc-item" style="top:190px"><div class="txt"><strong>LOREM IPSUM</strong>Curabitur sed felis eleifend,<br>porta nisl id, pretium ante.<br>Cras tincidunt efficitur pretium.</div><div class="num"><small>PG</small>3</div></div>
    <div class="toc-item" style="top:245px"><div class="txt"><strong>LOREM IPSUM</strong>Curabitur sed felis eleifend,<br>porta nisl id, pretium ante.<br>Cras tincidunt efficitur pretium.</div><div class="num"><small>PG</small>4</div></div>
    <div class="toc-item" style="top:298px"><div class="txt"><strong>LOREM IPSUM</strong>Curabitur sed felis eleifend,<br>porta nisl id, pretium ante.<br>Cras tincidunt efficitur pretium.</div><div class="num"><small>PG</small>5</div></div>
    <div class="toc-item" style="top:351px"><div class="txt"><strong>LOREM IPSUM</strong>Curabitur sed felis eleifend,<br>porta nisl id, pretium ante.<br>Cras tincidunt efficitur pretium.</div><div class="num"><small>PG</small>6</div></div>
  </div>
</section>

<section class="spread" style="left:8px;top:530px;width:580px;height:408px" aria-label="Feature spread">
  <div class="page feature-left stripes">
    <div class="abs title heading">Title</div>
    <div class="abs body-copy on-red col-a"><p>Lorem ipsum dolor sit amet, consectetur adipiscing elit. Donec gravida posuere nunc in luctus. Quisque tincidunt malesuada maximus. Nam viverra nibh ante, quis malesuada elit pretium vel. Vivamus pellentesque eros id enim laoreet porttitor. Praesent id efficitur lacus. Duis elementum enim et commodo lacinia. Suspendisse elit urna, sagittis a quam vel, iaculis tincidunt turpis. In hac habitasse platea dictumst. Sed vulputate purus tellus, ac mattis lorem consequat ut. Ut cursus mi eget orci ornare fringilla. Morbi lacinia arcu sed nisi finibus luctus. Sed neque leo, sodales eu ante sagittis.</p></div>
    <div class="abs body-copy on-red col-b"><p>Duis congue augue vel est hendrerit mattis sit amet et ante. Vestibulum vulputate semper blandit. Pellentesque tempor aliquet diam sit amet interdum.</p></div>
    <div class="abs body-copy on-red col-c"><p>Vivamus molestie ac orci quis condimentum. Nullam varius, quam non porta accumsan, est ligula vestibulum turpis, eu facilisis lorem nibh vitae libero. In id justo mollis, eleifend elit in, faucibus diam. Ut varius dolor in erat faucibus.</p></div>
    <div class="abs drone-photo" role="img" aria-label="Photo of a drone silhouetted against a sunset sky"></div>
    <div class="abs quote">“Ut cursus mi eget orci ornare fringilla. Morbi lacinia arcu sed nisi finibus luctus.”</div>
    <div class="page-no light" style="left:8px"><b>PG</b>3<i></i></div>
  </div>
  <div class="page feature-right">
    <div class="photo" style="left:-125px;top:0;width:385px;height:198px;background:radial-gradient(circle at 30% 55%,#7a3a3a 0%,#3a1e2a 30%,#1a1020 60%,#0c0a12 100%)" role="img" aria-label="Photo of a camera viewfinder screen with warm bokeh lights behind"></div>
    <div class="abs title heading">Title</div>
    <div class="abs body-copy col-d">
      <p>Donec blandit pharetra finibus. Phasellus egestas tortor vitae lacinia tincidunt. Proin quis nisi tortor. Pellentesque urna mi, convallis id viverra sit amet, hendrerit nec magna. Cras vehicula mi sem, eget dapibus nunc venenatis a. Suspendisse condimentum, metus luctus pellentesque maximus, ipsum tortor accumsan nisi, eget euismod est orci ac sem. Nulla facilisi. Maecenas quis sem ac ligula consectetur lobortis mollis a nisl. Ut ac dui nec nisi euismod interdum in at erat. Aliquam fermentum suscipit nisl ut euismod. Etiam eget tempus augue, in mattis ligula.</p>
      <p>Ut dapibus erat nec velit euismod pretium eget feugiat orci. Morbi a tortor urna. In ultricies velit vitae turpis malesuada, vitae gravida dui venenatis. Proin ultricies est non placerat posuere. Aliquam mattis consequat tortor, eget sollicitudin ex dignissim.</p>
    </div>
    <div class="abs callout">Etiam eu eleifend lacus, in varius turpis. Donec aliquet sapien dignissim dui commodo, in dapibus quam pharetra. Integer vehicula, ligula vel congue ultricies tortor neque feugiat sem, non mattis risus ligula eget felis.</div>
    <div class="page-no" style="right:10px;flex-direction:row-reverse"><b>PG</b>4<i></i></div>
  </div>
</section>

<section class="spread" style="left:612px;top:530px;width:580px;height:408px" aria-label="Data spread">
  <div class="page data-left">
    <svg class="abs" style="left:0;top:0" width="290" height="408" aria-hidden="true">
      <polygon points="0,60 120,0 170,0 0,100" fill="#f3c3c9" opacity=".5"/>
      <polygon points="0,230 290,90 290,120 0,260" fill="#f3c3c9" opacity=".35"/>
      <polygon points="0,380 290,250 290,270 0,400" fill="#f3c3c9" opacity=".35"/>
    </svg>
    <div class="abs title heading">Title</div>
    <div class="abs body-copy col-e"><p>Lorem ipsum dolor sit amet, consectetur adipiscing elit. Donec gravida posuere nunc in luctus. Quisque tincidunt malesuada maximus. Nam viverra nibh ante, quis malesuada elit pretium vel. Vivamus pellentesque eros id enim laoreet porttitor. Praesent id efficitur lacus. Duis elementum enim et commodo lacinia. Suspendisse elit urna, sagittis a quam vel, iaculis tincidunt turpis. In hac habitasse platea dictumst. Sed vulputate purus tellus, ac mattis lorem consequat ut. Ut cursus mi eget orci ornare fringilla. Sed neque leo, sodales eu ante sagittis.</p></div>
    <div class="abs body-copy col-f"><p>Duis congue augue vel est hendrerit mattis sit amet et ante. Vestibulum vulputate semper blandit. Pellentesque tempor aliquet diam sit amet interdum.</p></div>
    <div class="abs lights-photo" role="img" aria-label="Photo of two studio spotlights on stands"></div>
    <div class="abs body-copy col-g"><p>Vivamus molestie ac orci quis condimentum. Nullam varius, quam non porta accumsan, est ligula vestibulum turpis, eu facilisis lorem nibh vitae libero. In id justo mollis, eleifend elit in, faucibus diam. Ut varius dolor in erat faucibus.</p></div>
    <div class="abs title2 heading">Title</div>
    <div class="abs chart" aria-label="Bar chart">
      <div class="chart-row"><span>Lorem</span><div class="track"><div class="fill" style="width:62%;background:#f39ba3"></div></div></div>
      <div class="chart-row"><span>Lorem</span><div class="track"><div class="fill" style="width:78%;background:#ef6b76"></div></div></div>
      <div class="chart-row"><span>Lorem</span><div class="track"><div class="fill" style="width:56%;background:#e8424f"></div></div></div>
      <div class="chart-row"><span>Lorem</span><div class="track"><div class="fill" style="width:88%;background:#d0202e"></div></div></div>
      <div class="chart-row"><span>Lorem</span><div class="track"><div class="fill" style="width:30%;background:#c01a27"></div></div></div>
      <div class="chart-row"><span>Lorem</span><div class="track"><div class="fill" style="width:95%;background:#a8141f"></div></div></div>
      <div class="chart-row"><span>Lorem</span><div class="track"><div class="fill" style="width:58%;background:#8e0f18"></div></div></div>
      <div class="chart-row"><span>Lorem</span><div class="track"><div class="fill" style="width:42%;background:#6e0b13"></div></div></div>
    </div>
    <div class="abs body-copy col-h"><p>Nunc accumsan cursus nibh. Quisque non felis nec sem porttitor mollis. In tellus nibh, faucibus sed varius ut, blandit et ante. Donec porttitor neque sed tellus tempor, eget blandit nibh auctor. Curabitur dapibus dolor nec ipsum ultricies elementum. Nam lectus purus, lacinia non finibus at, pellentesque vel nisl.</p></div>
    <div class="page-no" style="left:8px"><b>PG</b>5<i></i></div>
  </div>
  <div class="page data-right" role="img" aria-label="Photo of a smiling camera operator beside a broadcast camera on a tripod at an outdoor event">
    <div class="abs quote">“Morbi lacinia arcu sed nisi finibus luctus.”</div>
    <div class="page-no light" style="right:10px;flex-direction:row-reverse"><b>PG</b>6<i></i></div>
  </div>
</section>

</body>
</html>
```